Business Card design for a skin clinic

i would like a business card design for our skin clinic.
our logo colors are Blue and Grey and Bule /white.
we are searching for a minimalistic design yet very elegant,dynamic and professional which can reflect a professional medical skin care clinic( not a beauty salon).
THE DESGIN IS NOT FOR A PERSON IT WILL BE USED IN THE CLINIC FOR CLIENTS SO THERE SHOULD BE NO NAME OF A PERSON ONLY THE CLINIC NAME AND THE CONTACT INFO

Target Market(s)
young and old womens
Industry/Entity Type
Business
Contact Information for Business Card
we have 2 address and both should be on the card.
address A: Lindenhoflaan 214B, 3041KP Rotterdam, Tel 010 483 21 95
address B: Zonnewijzerstraat 238, 1062RT Amsterdam Tel 020 571 3829
website www.huidpuntzorg.nu, email info@huidpuntzorg.nu
Look and feel
Each slider illustrates characteristics of the customer's brand and the style your logo design should communicate.

```html
<!DOCTYPE html>
<html lang="nl">
<head>
<meta charset="utf-8">
<title>Huidpuntzorg – business card</title>
<link href="https://fonts.googleapis.com/css2?family=Jost:wght@400;500&display=swap" rel="stylesheet">
<style>
  :root {
    --backdrop: #f1ecd2;
    --front-blue: #8dcfe5;
    --front-pattern: #7cc4de;
    --back-blue: #d3e9f1;
    --back-pattern: #b9dbe8;
    --brand-blue: #1f72b8;
    --ink-grey: #4a4d55;
    --tag-grey: #5d6b75;
    --shadow: rgba(60, 70, 60, 0.18);
  }
  * { margin: 0; padding: 0; box-sizing: border-box; }
  html, body { width: 1200px; height: 878px; overflow: hidden; }
  body {
    background: var(--backdrop);
    font-family: "Jost", "Futura", sans-serif;
    position: relative;
  }
  .card {
    position: absolute;
    top: 271px;
    width: 520px;
    height: 336px;
    overflow: hidden;
    box-shadow: 0 10px 24px var(--shadow);
  }
  .card--front { left: 50px; background: var(--front-blue); }
  .card--back  { left: 630px; background: var(--back-blue); }

  .pattern-fill { position: absolute; }
  .card--front .pattern-fill {
    inset: 0;
    background: linear-gradient(135deg, var(--front-pattern), var(--front-blue) 60%, var(--front-pattern));
  }
  .card--back .pattern-fill {
    left: 0; top: 0; bottom: 0; width: 230px;
    background: linear-gradient(90deg, var(--back-pattern), var(--back-blue));
  }

  .brand {
    position: absolute;
    left: 0; right: 0; top: 130px;
    text-align: center;
  }
  .brand__row { display: inline-flex; align-items: center; gap: 12px; }
  .brand__dot {
    width: 14px; height: 14px; border-radius: 50%;
    background: var(--brand-blue);
  }
  .brand__name {
    font-size: 38px; font-weight: 400; letter-spacing: 3px;
    color: var(--brand-blue); text-transform: uppercase;
  }
  .brand__tagline {
    margin-top: 4px;
    font-size: 13px; letter-spacing: 2px;
    color: var(--tag-grey); text-transform: lowercase;
  }

  .contact {
    position: absolute;
    right: 38px; top: 44px;
    text-align: right;
    font-style: normal;
    font-size: 17px; line-height: 1.25;
    color: var(--ink-grey);
  }
  .contact__street { color: var(--brand-blue); }
  .contact__label { color: var(--brand-blue); font-weight: 500; }
  .contact__block { margin-bottom: 16px; }
  .contact__web { margin-top: 6px; }
</style>
</head>
<body>
  <section class="card card--front" aria-label="Card front">
    <div class="pattern-fill" role="img" aria-label="Repeating outline pattern of rounded hexagonal shapes in light blue"></div>
    <div class="brand">
      <div class="brand__row">
        <span class="brand__dot"></span>
        <span class="brand__name">Huidpuntzorg</span>
      </div>
      <p class="brand__tagline">clinical care for healthy skin</p>
    </div>
  </section>

  <section class="card card--back" aria-label="Card back">
    <div class="pattern-fill" role="img" aria-label="Fading outline pattern of rounded hexagonal shapes in pale blue"></div>
    <address class="contact">
      <div class="contact__block">
        <div class="contact__street">Lindenhoflaan 214B</div>
        <div>3041KP Rotterdam</div>
        <div><span class="contact__label">Tel</span> 010 483 21 95</div>
      </div>
      <div class="contact__block">
        <div class="contact__street">Zonnewijzerstraat 238</div>
        <div>1062RT Amsterdam</div>
        <div><span class="contact__label">Tel</span> 020 571 3829</div>
      </div>
      <div class="contact__web">www.huidpuntzorg.nu</div>
      <div>info@huidpuntzorg.nu</div>
    </address>
  </section>
</body>
</html>
```